Neues Corporate Identity Web Design für einen coolen Energydrink
Zielgruppe
UPDATE: das BETA storyboard für das Video auf der neuen Seite.. jetzt in den Dateien, hier fehlt noch der sportliche dynamische abenteurliche part.. wird die tage erneut geupdatet..
Hallo Designer,
wir sind Velunora - ein junges Start-Up, die 'Guayusa - den Energydrink der Indianer' nach Deutschland gebracht haben. Mit unseren Produkten sprechen wir Backpacker / Abenteurer, Gesundheitsbewusste, Spirituelle, Kreative, Startups, Surfer, Skater, Weltverbesserer, Hipster und später auch Sportler und Gamer an. Und klaro auch die Energydrink und Kaffeejunkies ;-) ...
Aufgabenstellung
Neues Corporate Identity Design für eine Wordpress Seite mit Shop Funktion (Woocomerce)
Ihr findet eine PDF in den Dateien mit den genauen Wünschen von uns. -> BITTE LESEN!
Bilder könnt Ihr aus den bestehenden Auftritten entnehmen. Ihr findet diese auf unser Webseite: www.velunora.de auf unserem Facebook Account: www.facebook.com/Kolarintee/ auf unserem Instagram Account: www.instagram.com/velunora als auch auf unseren Produktseiten auf Kaufstadt. Weitere Bilder können aus bildervorrat-beispiel.de vorgeschlagen werden.
Die von uns verwendete Schriftart haben wir auch angehängt, ist aber kein Muss, wenn ihr andere Ideen habt, her damit!
Dateiübergabe in PSD Form, so das ein Webdesigner es gut umsetzen kann.

```html
<!DOCTYPE html>
<html lang="de">
<head>
<meta charset="utf-8">
<title>Velunora – Energy Kick aus dem Amazonas</title>
<link rel="stylesheet" href="https://fonts.googleapis.com/css2?family=Montserrat:wght@300;400;600;700;800&display=swap">
<style>
:root{
  --tan:#d3a877;
  --tan-dark:#b98a57;
  --ink:#2b2b2b;
  --muted:#777;
  --nav:#232323;
  --green:#8cc63f;
  --paper:#ffffff;
  --stage:#e9e9e9;
  --line:#d8d8d8;
}
*{box-sizing:border-box;margin:0;padding:0}
html,body{width:1200px;height:900px;overflow:hidden}
body{background:var(--stage);font-family:"Montserrat",sans-serif;color:var(--ink);position:relative}
.page{position:absolute;top:30px;width:560px;height:840px;background:var(--paper);box-shadow:0 6px 18px rgba(0,0,0,.12);overflow:hidden;display:flex;flex-direction:column}
.page--left{left:30px}
.page--right{left:610px}

/* header */
.site-header{height:52px;flex:none}
.topbar{height:30px;display:flex;align-items:center;justify-content:space-between;padding:0 18px}
.brand{display:flex;align-items:center;gap:6px;font-weight:800;font-size:13px;letter-spacing:2px;color:var(--tan)}
.brand__mark{width:10px;height:10px;background:var(--tan)}
.tools{display:flex;gap:8px}
.tools svg{width:10px;height:10px}
.main-nav{height:22px;background:var(--nav);display:flex;align-items:center;padding:0 18px;gap:16px}
.main-nav a{font-size:6.5px;color:#ddd;text-decoration:none;letter-spacing:.5px}
.main-nav a.is-active{background:var(--tan);color:#fff;padding:5px 7px}

/* photo fills */
.photo{position:relative}
.photo--hills{background:linear-gradient(180deg,#8a8f80 0%,#5f7f59 40%,#3e6a36 75%,#6c8e3c 100%)}
.photo--forest{background:linear-gradient(120deg,#dfe6d6 0%,#9fb98a 45%,#4f7a3b 100%)}
.photo--tea{background:radial-gradient(circle at 50% 55%,#a9d24a 0%,#6aa13a 40%,#fff 72%)}
.photo--leaves{background:linear-gradient(140deg,#6f645a,#3c342d 60%,#5f7d3a)}
.photo--stone{background:linear-gradient(160deg,#5b8f3a 0%,#6f6a60 45%,#8a7c6c 100%)}
.photo--writing{background:linear-gradient(110deg,#9a4c2a,#c78a55 45%,#e9e1d3 80%)}
.photo--terraces{background:linear-gradient(90deg,#6d8b3a,#93a85a 50%,#5d7a35)}

/* hero */
.hero{height:210px;flex:none;display:flex;flex-direction:column;align-items:center;justify-content:center;gap:14px}
.hero__title{color:#fff;font-weight:800;font-size:24px;text-align:center;line-height:1.25;letter-spacing:.5px;text-shadow:0 1px 3px rgba(0,0,0,.3)}
.btn{display:inline-block;border:1px solid var(--ink);font-size:7px;letter-spacing:1px;padding:5px 14px;background:#fff;color:var(--ink)}
.btn--ghost{border-color:#fff;color:#fff;background:transparent}

/* why */
.why{height:190px;flex:none;display:flex;align-items:center;padding:0 34px;gap:26px}
.why__image{width:210px;height:150px;flex:none}
.why__title{font-weight:800;font-size:20px;letter-spacing:.5px;margin-bottom:14px}
.why__list{list-style:none;margin-bottom:14px}
.why__list li{display:flex;gap:8px;font-size:11px;line-height:1.3;margin-bottom:8px}
.why__list svg{flex:none;width:9px;height:11px;margin-top:2px}

/* meaning */
.meaning{height:130px;flex:none;background:var(--tan);display:flex;align-items:center;padding:0 28px;gap:20px}
.meaning p{color:#fff;font-size:9.5px;line-height:1.55;font-weight:400}
.meaning strong{font-weight:700}
.meaning__figure{width:90px;height:90px;flex:none;border-radius:50%;background:rgba(255,255,255,.22)}

.slogan{height:50px;flex:none;display:flex;align-items:center;justify-content:center;gap:10px;font-weight:300;font-size:18px;color:#444}
.slogan svg{width:9px;height:11px}

.hero2{flex:1;display:flex;align-items:center;justify-content:flex-end;padding-right:40px}
.hero2__title{color:#fff;font-weight:800;font-size:24px;line-height:1.25;text-shadow:0 1px 3px rgba(0,0,0,.3)}

/* products */
.products{height:250px;flex:none;padding:16px 26px 0;text-align:center}
.section-title{font-weight:600;font-size:15px;letter-spacing:1px}
.section-sub{font-size:8px;color:var(--muted);margin:4px auto 12px;max-width:300px;line-height:1.4}
.product-grid{display:flex;gap:14px}
.product{flex:1;border:1px solid var(--line);text-align:left}
.product__image{height:82px}
.product__body{padding:8px 10px}
.product__name{font-size:7px;font-weight:700;color:var(--tan);letter-spacing:.5px}
.product__text{font-size:6.5px;color:var(--muted);line-height:1.45;margin:5px 0 7px}
.product .btn{font-size:6px;padding:3px 10px}

/* categories */
.categories{height:90px;flex:none;display:flex}
.category{flex:1;display:flex;flex-direction:column;align-items:center;justify-content:center;gap:6px;color:#fff;font-size:8px;font-weight:600;letter-spacing:1px;text-align:center;border-right:1px solid rgba(255,255,255,.25)}
.category svg{width:18px;height:14px}

/* blog */
.blog{height:250px;flex:none;padding:18px 26px 0;text-align:center}
.blog-grid{display:flex;gap:12px;margin-top:14px}
.post{flex:1;border:1px solid var(--line);text-align:left;box-shadow:0 2px 5px rgba(0,0,0,.06)}
.post__image{height:86px}
.post__body{padding:8px 9px}
.post__title{font-size:7px;font-weight:700;color:var(--tan)}
.post__date{font-size:6px;color:var(--muted);margin-top:2px}
.post__text{font-size:6.5px;color:var(--muted);line-height:1.45;margin:5px 0 8px}
.post .btn{font-size:6px;padding:3px 10px}

/* newsletter */
.newsletter{height:200px;flex:none;display:flex;flex-direction:column;align-items:center;justify-content:center;gap:10px}
.newsletter__title{color:#fff;font-weight:600;font-size:18px;letter-spacing:1.5px}
.newsletter__form{display:flex}
.newsletter__input{width:200px;height:20px;background:rgba(255,255,255,.9);font-size:7px;color:var(--muted);padding:6px 8px}
.newsletter__submit{height:20px;background:var(--tan);color:#fff;font-size:7px;padding:6px 10px;letter-spacing:1px}

.site-footer{flex:1;display:flex;justify-content:space-around;align-items:center;font-size:7px;font-weight:700;letter-spacing:1px;border-top:1px solid var(--line)}
</style>
</head>
<body>

<main class="page page--left">
  <header class="site-header">
    <div class="topbar">
      <div class="brand"><span class="brand__mark"></span>VELUNORA</div>
      <div class="tools">
        <svg viewBox="0 0 10 10"><circle cx="5" cy="3" r="2.2" fill="var(--tan)"/><path d="M1 10c0-3 8-3 8 0z" fill="var(--tan)"/></svg>
        <svg viewBox="0 0 10 10"><circle cx="4" cy="4" r="3" fill="none" stroke="#555" stroke-width="1.2"/><path d="M6.2 6.2L9 9" stroke="#555" stroke-width="1.2"/></svg>
        <svg viewBox="0 0 10 10"><path d="M1 2h2l1.2 5h4.3L9.5 3.5H3.5" fill="none" stroke="#555" stroke-width="1"/></svg>
      </div>
    </div>
    <nav class="main-nav">
      <a class="is-active">HOME</a><a>ÜBER GUAYUSA</a><a>PRODUKTE</a><a>VELUNORA STORY</a><a>BLOG</a>
    </nav>
  </header>

  <section class="hero photo photo--hills" role="img" aria-label="Nebelige grüne Berglandschaft mit Teeterrassen im Amazonasgebiet">
    <h1 class="hero__title">Velunora: Energy Kick<br>aus dem Amazonas</h1>
    <span class="btn btn--ghost">ZUM SHOP</span>
  </section>

  <section class="why">
    <div class="why__image photo photo--tea" role="img" aria-label="Glastasse mit grünem Guayusa-Tee und frischen Blättern"></div>
    <div>
      <h2 class="why__title">WARUM GUAYUSA?</h2>
      <ul class="why__list">
        <li><svg viewBox="0 0 9 11"><path d="M1 10C1 5 4 1 8 1c0 5-3 9-7 9z" fill="var(--green)"/></svg><span>100% <b>handmade</b> by<br>Quechua Indianern</span></li>
        <li><svg viewBox="0 0 9 11"><path d="M1 10C1 5 4 1 8 1c0 5-3 9-7 9z" fill="var(--green)"/></svg><span>mehr <b>Koffein</b> als Kaffe</span></li>
        <li><svg viewBox="0 0 9 11"><path d="M1 10C1 5 4 1 8 1c0 5-3 9-7 9z" fill="var(--green)"/></svg><span>leistung ausdauer<br>&amp; <b>konzentration</b></span></li>
      </ul>
      <span class="btn">WARUM GUAYUSA?</span>
    </div>
  </section>

  <section class="meaning">
    <p><strong>Velunora</strong> bedeutet in der Quichua Sprache <strong>„Andere Welt“</strong>. Das Logo ist eine Figur mit anscheinend nur einem Auge, denn das andere ist geschlossen, da der Schamane „Velunyn“ ist. Er trank Guayusa und so ist er mit einem Auge in dieser Welt und mit dem anderen in der „Andere Welt“.</p>
    <div class="meaning__figure" role="img" aria-label="Illustration der Schamanenfigur"></div>
  </section>

  <section class="slogan">
    <svg viewBox="0 0 9 11"><path d="M1 10C1 5 4 1 8 1c0 5-3 9-7 9z" fill="var(--green)"/></svg>
    <span>Sei nicht müde - Sei Velunora!</span>
    <svg viewBox="0 0 9 11"><path d="M1 10C1 5 4 1 8 1c0 5-3 9-7 9z" fill="var(--green)"/></svg>
  </section>

  <section class="hero2 photo photo--forest" role="img" aria-label="Wanderer mit orangem Rucksack im Wald">
    <h2 class="hero2__title">Lorem ipsum<br>dolor sit loremit</h2>
  </section>
</main>

<main class="page page--right">
  <section class="products">
    <h2 class="section-title">VELUNORA GUAYUSA ENERGY</h2>
    <p class="section-sub">Duis aute irure dolor in reprehenderit in voluptate velit esse cillum dolore eu fugiat nulla pariatur</p>
    <div class="product-grid">
      <article class="product">
        <div class="product__image photo photo--leaves" role="img" aria-label="Holzschale mit getrockneten Guayusa-Blättern"></div>
        <div class="product__body">
          <div class="product__name">VELUNORA GUAYUSA ENERGY TEE</div>
          <p class="product__text">Lose Blätter, schonend getrocknet und von Hand verlesen. Ein milder Aufguss mit natürlichem Koffein, der lange wach hält und dabei sanft bleibt. Ideal für den Morgen.</p>
          <span class="btn">ZUM WARENKORB</span>
        </div>
      </article>
      <article class="product">
        <div class="product__image photo photo--leaves" role="img" aria-label="Schalen mit Guayusa-Tee und frischen grünen Blättern"></div>
        <div class="product__body">
          <div class="product__name">VELUNORA GUAYUSA ENERGY PADS</div>
          <p class="product__text">Praktische Pads für unterwegs, einfach aufgießen und genießen. Die Energie der Blätter in handlicher Form, ganz ohne Zucker und künstliche Zusätze.</p>
          <span class="btn">ZUM WARENKORB</span>
        </div>
      </article>
    </div>
  </section>

  <section class="categories photo photo--terraces" role="img" aria-label="Grüne Teeterrassen als Hintergrund der Kategorien">
    <div class="category">UNSERE<br>GESICHTE<svg viewBox="0 0 18 14"><path d="M1 1h16L9 13z" fill="none" stroke="#fff"/></svg></div>
    <div class="category">TEAM &amp; AUTHENTISCH<br>VOR ORT<svg viewBox="0 0 18 14"><path d="M1 1h16L9 13z" fill="none" stroke="#fff"/></svg></div>
    <div class="category">STIFTUNG &amp;<br>HILFSPROJEKT<svg viewBox="0 0 18 14"><path d="M1 1h16L9 13z" fill="none" stroke="#fff"/></svg></div>
  </section>

  <section class="blog">
    <h2 class="section-title">NEUESTE BLOGBEITRÄGE</h2>
    <div class="blog-grid">
      <article class="post">
        <div class="post__image photo photo--stone" role="img" aria-label="Felsen mit eingeritzter Petroglyphe"></div>
        <div class="post__body">
          <div class="post__title">GUAYUSA'S PETROGLYPHE</div>
          <div class="post__date">12.05.2018</div>
          <p class="post__text">Mitten im Dschungel des Amazonas liegt ein großer Stein mit geheimnisvollen Zeichnungen, die uns viel erzählen.</p>
          <span class="btn">WEITER LESEN</span>
        </div>
      </article>
      <article class="post">
        <div class="post__image photo photo--stone" role="img" aria-label="Felsen mit eingeritzter Petroglyphe"></div>
        <div class="post__body">
          <div class="post__title">GUAYUSA'S PETROGLYPHE</div>
          <div class="post__date">12.05.2018</div>
          <p class="post__text">Mitten im Dschungel des Amazonas liegt ein großer Stein mit geheimnisvollen Zeichnungen, die uns viel erzählen.</p>
          <span class="btn">WEITER LESEN</span>
        </div>
      </article>
      <article class="post">
        <div class="post__image photo photo--stone" role="img" aria-label="Felsen mit eingeritzter Petroglyphe"></div>
        <div class="post__body">
          <div class="post__title">GUAYUSA'S PETROGLYPHE</div>
          <div class="post__date">12.05.2018</div>
          <p class="post__text">Mitten im Dschungel des Amazonas liegt ein großer Stein mit geheimnisvollen Zeichnungen, die uns viel erzählen.</p>
          <span class="btn">WEITER LESEN</span>
        </div>
      </article>
    </div>
  </section>

  <section class="newsletter photo photo--writing" role="img" aria-label="Hand mit Stift schreibt in ein Notizbuch">
    <h2 class="newsletter__title">NEWSLETTER</h2>
    <div class="newsletter__form">
      <span class="newsletter__input">E-Mail</span>
      <span class="newsletter__submit">ABSENDEN</span>
    </div>
  </section>

  <footer class="site-footer">
    <span>VELUNORA</span><span>SERVICE</span><span>KONTAKT</span>
  </footer>
</main>

</body>
</html>
```